Corporate A4 Advert for Worldwide Timber Trader/Agent

We need a new professional company ad, which will be used in worldwide magazine publications. something sophisticated.
Our website - www.qrolumber.co.uk - for info. We are timber agents and sell timber from one part of the world to another.
I will upload a selection of product photos to include - suggest using not all but a selection of some them, to showcase the product. Our buyers purchase both logs and sawn timber
We would like this ad to list our source areas and product groups.
Our company colour is British Racing Green
Updates

Target Market(s)

timber buyers

Industry/Entity Type

Timber

Colors
00AB8E
00BBA5
67D7C9
C6EFE9
E9F9F6

Requirements
Must have
• company logo

```html
<!DOCTYPE html>
<html lang="en">
<head>
<meta charset="utf-8">
<title>QRO — Global Timber Sourcing &amp; Distribution</title>
<link rel="stylesheet" href="https://fonts.googleapis.com/css2?family=Outfit:wght@400;600;700;800&family=Figtree:wght@400;500&display=swap">
<style>
  :root {
    --racing-green: #2a3128;
    --leaf-green: #3f7a2e;
    --sage: #cfd2a6;
    --paper: #f3f3f1;
    --paper-shade: #e4e4e2;
    --ink: #1f231f;
    --wood: #b85b2b;
    --wood-deep: #8e3f1c;
    --wood-light: #d58a57;
    --forest: #5b6b4c;
  }
  * { margin: 0; padding: 0; box-sizing: border-box; }
  html, body { width: 900px; height: 1200px; overflow: hidden; background: var(--paper); }
  .advert {
    position: relative; width: 900px; height: 1200px; overflow: hidden;
    font-family: "Figtree", sans-serif; color: var(--ink);
  }
  .backdrop {
    position: absolute; inset: 0;
    background: linear-gradient(160deg, #f6f6f4 0%, #ececea 45%, #e6e6e4 70%, #f4f4f2 100%);
  }
  .shapes { position: absolute; inset: 0; }
  .brand {
    position: absolute; left: 70px; top: 110px; width: 170px;
    display: flex; flex-direction: column; align-items: center; gap: 14px;
  }
  .brand-dot { width: 96px; height: 96px; border-radius: 50%; background: var(--ink); }
  .brand-name {
    font-family: "Outfit", sans-serif; font-weight: 800; font-size: 58px;
    line-height: 1; letter-spacing: 1px; color: var(--ink);
  }
  .headline {
    position: absolute; left: 352px; top: 50px;
    font-family: "Outfit", sans-serif; font-weight: 800; font-size: 56px;
    line-height: 52px; letter-spacing: -0.5px; color: var(--racing-green);
  }
  .intro {
    position: absolute; left: 424px; top: 325px; width: 330px;
    font-size: 15.5px; line-height: 21px; color: var(--ink);
  }
  .product-list {
    position: absolute; left: 518px; top: 413px; list-style: none;
    font-family: "Outfit", sans-serif; font-weight: 700; font-size: 20px;
    color: var(--leaf-green); letter-spacing: 0.2px;
  }
  .product-list li { display: flex; align-items: center; gap: 8px; height: 25.5px; }
  .product-list svg { width: 16px; height: 16px; flex: none; }
  .services-title {
    position: absolute; left: 516px; top: 640px;
    font-family: "Outfit", sans-serif; font-weight: 800; font-size: 38px;
    color: var(--racing-green); letter-spacing: 0.5px;
  }
  .service-list {
    position: absolute; left: 518px; top: 698px; list-style: none;
    font-family: "Outfit", sans-serif; font-size: 17px; color: var(--ink);
  }
  .service-list li { display: flex; gap: 10px; line-height: 21px; margin-bottom: 13px; }
  .service-list .bullet {
    flex: none; width: 10px; height: 10px; margin-top: 6px;
    background: var(--racing-green); transform: rotate(45deg);
  }
  .contact-title {
    position: absolute; left: 516px; top: 965px;
    font-family: "Outfit", sans-serif; font-weight: 800; font-size: 27px;
    color: var(--racing-green);
  }
  .contact-lines {
    position: absolute; left: 516px; top: 1010px;
    font-family: "Outfit", sans-serif; font-weight: 600; font-size: 21px;
    line-height: 28.5px; color: var(--ink);
  }
</style>
</head>
<body>
<main class="advert">
  <div class="backdrop" role="img" aria-label="Faint background photograph of a sawmill interior with machinery"></div>

  <svg class="shapes" viewBox="0 0 900 1200" width="900" height="1200" aria-hidden="false">
    <defs>
      <linearGradient id="wood" x1="0" y1="0" x2="1" y2="1">
        <stop offset="0" stop-color="#c9713f"/>
        <stop offset="0.55" stop-color="#b85b2b"/>
        <stop offset="1" stop-color="#8e3f1c"/>
      </linearGradient>
      <linearGradient id="wood-yard" x1="0" y1="0" x2="0" y2="1">
        <stop offset="0" stop-color="#7d8a6a"/>
        <stop offset="0.25" stop-color="#c8764a"/>
        <stop offset="1" stop-color="#b8552a"/>
      </linearGradient>
      <linearGradient id="mill-floor" x1="0" y1="0" x2="0" y2="1">
        <stop offset="0" stop-color="#d9d9d6"/>
        <stop offset="0.35" stop-color="#a8674a"/>
        <stop offset="1" stop-color="#9a5236"/>
      </linearGradient>
    </defs>

    <!-- top right accent triangles -->
    <polygon points="714,0 900,0 813,147" fill="var(--racing-green)"/>
    <polygon points="900,34 900,157 825,157" fill="var(--sage)"/>
    <polygon points="825,176 900,176 900,303" fill="var(--leaf-green)"/>

    <!-- photo mosaic -->
    <polygon points="0,324 300,324 129,607 0,432" fill="url(#wood-yard)" role="img" aria-label="Photo of stacked hardwood logs at a forest yard"/>
    <polygon points="321,324 152,607 504,607" fill="url(#wood)" role="img" aria-label="Photo of a worker stencilling the company mark onto sawn timber"/>
    <polygon points="134,625 297,903 0,903 0,720" fill="url(#wood)" role="img" aria-label="Photo of banded packs of sawn timber on red earth"/>
    <polygon points="150,621 504,621 320,903" fill="url(#wood-yard)" role="img" aria-label="Photo of sawn timber packs at a log yard with trucks"/>
    <polygon points="0,916 297,916 134,1194 0,960" fill="url(#wood)" role="img" aria-label="Photo of large hardwood log ends marked with numbers"/>
    <polygon points="320,919 150,1200 504,1200" fill="url(#mill-floor)" role="img" aria-label="Photo of band saw blades coiled on a sawmill floor"/>

    <!-- connector line -->
    <polyline points="357,324 532,600 863,600" fill="none" stroke="var(--ink)" stroke-width="1.3"/>
    <polygon points="352,320 357,316 362,320 362,328 357,332 352,328" fill="var(--ink)" transform="rotate(30 357 324)"/>
    <polygon points="858,596 863,592 868,596 868,604 863,608 858,604" fill="var(--ink)" transform="rotate(30 863 600)"/>

    <!-- bottom band -->
    <polygon points="387,992 422,992 545,1200 512,1200" fill="var(--racing-green)"/>
    <polygon points="777,992 900,992 900,1166" fill="var(--racing-green)"/>
  </svg>

  <div class="brand">
    <span class="brand-dot"></span>
    <span class="brand-name">QRO</span>
  </div>

  <h1 class="headline">GLOBAL<br>TIMBER<br>SOURCING &amp;<br>DISTRIBUTION</h1>

  <p class="intro">we take pride in trading timber globally and responsibly. Developing and nurturing clients and suppliers is critical to our success</p>

  <ul class="product-list">
    <li><svg viewBox="0 0 16 16"><circle cx="8" cy="8.5" r="6.2" fill="none" stroke="#1f231f" stroke-width="1.4"/><path d="M4.6 8.4 7.3 11 14.5 2.5" fill="none" stroke="#1f231f" stroke-width="1.6" stroke-linecap="round"/></svg>HARDWOODS</li>
    <li><svg viewBox="0 0 16 16"><circle cx="8" cy="8.5" r="6.2" fill="none" stroke="#1f231f" stroke-width="1.4"/><path d="M4.6 8.4 7.3 11 14.5 2.5" fill="none" stroke="#1f231f" stroke-width="1.6" stroke-linecap="round"/></svg>SOFTWOOD</li>
    <li><svg viewBox="0 0 16 16"><circle cx="8" cy="8.5" r="6.2" fill="none" stroke="#1f231f" stroke-width="1.4"/><path d="M4.6 8.4 7.3 11 14.5 2.5" fill="none" stroke="#1f231f" stroke-width="1.6" stroke-linecap="round"/></svg>LOGS</li>
    <li><svg viewBox="0 0 16 16"><circle cx="8" cy="8.5" r="6.2" fill="none" stroke="#1f231f" stroke-width="1.4"/><path d="M4.6 8.4 7.3 11 14.5 2.5" fill="none" stroke="#1f231f" stroke-width="1.6" stroke-linecap="round"/></svg>BOULES</li>
    <li><svg viewBox="0 0 16 16"><circle cx="8" cy="8.5" r="6.2" fill="none" stroke="#1f231f" stroke-width="1.4"/><path d="M4.6 8.4 7.3 11 14.5 2.5" fill="none" stroke="#1f231f" stroke-width="1.6" stroke-linecap="round"/></svg>SEMI-FINISHED PRODUCTS</li>
    <li><svg viewBox="0 0 16 16"><circle cx="8" cy="8.5" r="6.2" fill="none" stroke="#1f231f" stroke-width="1.4"/><path d="M4.6 8.4 7.3 11 14.5 2.5" fill="none" stroke="#1f231f" stroke-width="1.6" stroke-linecap="round"/></svg>HEAT-TREATED TIMBER</li>
  </ul>

  <h2 class="services-title">SERVICES</h2>
  <ul class="service-list">
    <li><span class="bullet"></span><span>First hand market information<br>and product expertise</span></li>
    <li><span class="bullet"></span><span>Quality Control</span></li>
    <li><span class="bullet"></span><span>Reliable Shipments</span></li>
    <li><span class="bullet"></span><span>Payment Options</span></li>
    <li><span class="bullet"></span><span>Continuity of Supply</span></li>
    <li><span class="bullet"></span><span>Recognising your Individual needs</span></li>
    <li><span class="bullet"></span><span>Due Diligence</span></li>
  </ul>

  <h2 class="contact-title">CONTACT US</h2>
  <address class="contact-lines" style="font-style:normal">
    +44(0)20 7946 0321<br>
    sales@qrolumber.co.uk<br>
    www.qrolumber.co.uk
  </address>
</main>
</body>
</html>
```